Current wordpress website needs some additions & to be made more user friendly & visually...

Kindred Pathways Carers Network (KPCN) is a volunteer, not-for-profit organisation supporting parents & carers who are trying to support their loved one with a life-threatening eating disorder. We have a website www.kpcn-example.org.au which is in Wordpress & need to make membership registration & donations more obvious, streamlined, easy & efficient, as well as reducing how 'wordy' the page looks, by making it more visually appealing. Please refer to the look and feel and functionality of www.brightharbourhealthsupport-example.org.au. Please confirm if our site can look and function as per this site.

```html
<!DOCTYPE html>
<html lang="en">
<head>
<meta charset="utf-8">
<title>Kindred Pathways Carers Network</title>
<link href="https://fonts.googleapis.com/css2?family=Open+Sans:wght@400;600;700;800&display=swap" rel="stylesheet">
<style>
:root{
  --magenta:#9c1c6c;
  --plum:#6e1a63;
  --purple:#8a2a84;
  --green:#5cb82a;
  --green-dark:#3f9a17;
  --red:#c9152f;
  --blue:#2d5fb4;
  --grey-bg:#f1f1f1;
  --text:#333;
  --muted:#777;
  --white:#fff;
}
*{box-sizing:border-box;margin:0;padding:0}
html,body{width:1200px;height:4224px;overflow:hidden;background:var(--white)}
body{font-family:"Open Sans",Arial,sans-serif;color:var(--text);position:relative}
section,header,footer{position:absolute;left:0;width:1200px}
.btn{display:inline-block;border-radius:30px;color:#fff;font-weight:700;font-size:15px;text-transform:uppercase;padding:14px 34px;letter-spacing:.5px;white-space:nowrap}
.btn-green{background:var(--green)}
.btn-magenta{background:var(--magenta)}
.btn-small{font-size:13px;padding:10px 26px}

/* header */
.site-header{top:0;height:150px;background:#fff}
.brand{position:absolute;left:90px;top:16px;display:flex;align-items:center;gap:12px}
.brand-dot{width:44px;height:44px;border-radius:50%;background:var(--magenta)}
.brand-name{font-weight:700;font-size:15px;color:var(--plum);width:160px;line-height:1.2}
.top-links{position:absolute;right:90px;top:40px;display:flex;gap:22px;font-size:13px;color:var(--magenta);font-weight:600;align-items:center}
.top-links .social{width:14px;height:14px;border-radius:50%;background:var(--green)}
.main-nav{position:absolute;left:310px;top:100px;display:flex;gap:30px;font-size:14px;font-weight:700;color:var(--magenta);text-transform:uppercase}

/* hero */
.hero{top:150px;height:680px;overflow:hidden}
.hero-photo{position:absolute;inset:0;background:linear-gradient(135deg,#b09a8a 0%,#7e6c64 40%,#5b4c48 70%,#8b7466 100%)}
.hero-shade{position:absolute;inset:0;background:rgba(40,20,30,.25)}
.hero-title{position:absolute;top:140px;width:100%;text-align:center;color:#fff;font-size:46px;font-weight:800;text-transform:uppercase;line-height:1.15}
.hero-actions{position:absolute;top:290px;width:100%;display:flex;justify-content:center;gap:30px}
.hero-actions .btn{width:270px;text-align:center;font-size:15px;padding:14px 10px}
.save-date{position:absolute;left:440px;top:390px;width:320px;height:130px;border:2px solid #fff;border-radius:65px;color:#fff;text-align:center;padding-top:36px;font-size:14px;line-height:1.4}
.save-date strong{display:block;font-size:22px;font-weight:600;text-transform:uppercase}
.save-star{position:absolute;left:573px;top:360px}
.arrow{position:absolute;top:240px;width:44px;height:44px;border-radius:50%;background:rgba(255,255,255,.55)}
.arrow.left{left:90px}.arrow.right{right:90px}
.hero-curve{position:absolute;bottom:0;left:0}

/* about */
.about{top:830px;height:440px}
.about-art{position:absolute;left:140px;top:40px;width:320px;height:320px;border-radius:50%;background:radial-gradient(circle,#d98ab8 0%,#8f3f8a 60%,#4d6fb5 100%)}
.about-text{position:absolute;left:550px;top:40px;width:540px}
.about-text h2{font-size:34px;font-weight:800;color:var(--plum);margin-bottom:22px}
.about-text p{font-size:15px;line-height:1.75;margin-bottom:22px}

/* be informed */
.informed{top:1260px;height:540px}
.informed h2{position:absolute;top:80px;width:100%;text-align:center;color:#fff;font-size:30px;font-weight:800;text-transform:uppercase}
.pillars{position:absolute;top:160px;left:150px;width:900px;display:flex;justify-content:space-between}
.pillar{width:260px;text-align:center;color:#fff}
.pillar .circle{width:120px;height:120px;border-radius:50%;background:var(--green);border:4px solid #fff;margin:0 auto 22px}
.pillar h3{font-size:20px;font-weight:700;margin-bottom:10px}
.pillar p{font-size:13px;line-height:1.5;opacity:.9}
.pillar .more{width:42px;height:42px;border:2px solid #fff;border-radius:50%;margin:16px auto 0;display:flex;align-items:center;justify-content:center}

/* cards */
.cards{top:1860px;height:290px}
.card{position:absolute;top:0;width:440px;height:280px;border-radius:18px 18px 18px 60px;color:#fff;text-align:center;padding-top:76px}
.card h3{font-size:28px;font-weight:700;text-transform:uppercase;line-height:1.2;margin-bottom:12px}
.card p{font-size:14px;line-height:1.5;margin:0 auto 18px;width:320px}
.card-groups{left:150px;background:linear-gradient(160deg,#d81d44,#9b0d2a)}
.card-events{left:610px;background:linear-gradient(160deg,#3b77cc,#22468e)}

/* news */
.news{top:2200px;height:580px;background:var(--grey-bg)}
.news h2{position:absolute;top:100px;left:150px;font-size:30px;font-weight:800;color:var(--plum);text-transform:uppercase}
.news-grid{position:absolute;top:165px;left:150px;width:900px;display:flex;justify-content:space-between}
.news-item{width:270px}
.news-photo{height:170px;border-radius:4px;background:linear-gradient(135deg,#c9a58a,#8a6a55)}
.news-item h4{font-size:18px;font-weight:600;margin:14px 0 6px}
.news-date{font-size:14px;color:var(--blue);font-weight:600;margin-bottom:8px;display:flex;align-items:center;gap:6px}
.news-item p{font-size:12px;color:var(--muted);line-height:1.5;margin-bottom:16px}

/* volunteer */
.volunteer{top:2780px;height:480px}
.volunteer-text{position:absolute;left:160px;top:100px;width:500px}
.volunteer-text h2{font-size:34px;font-weight:800;color:var(--plum);text-transform:uppercase;line-height:1.15;margin-bottom:24px}
.volunteer-text p{font-size:15px;line-height:1.75;margin-bottom:26px}
.volunteer-photo{position:absolute;left:690px;top:50px;width:360px;height:360px;border-radius:50%;border:6px solid var(--magenta);background:linear-gradient(135deg,#b8b2aa,#6f6862)}

/* contact */
.contact{top:3260px;height:560px;overflow:hidden}
.contact-bg{position:absolute;inset:0;background:linear-gradient(135deg,#7cc63d,#4ea51c)}
.contact h2{position:absolute;top:150px;width:100%;text-align:center;color:#fff;font-size:30px;font-weight:800;text-transform:uppercase}
.field{position:absolute;height:56px;background:rgba(255,255,255,.28);border:1px solid rgba(255,255,255,.6);color:#fff;font-size:14px;padding:16px 18px}
.f-name{left:200px;top:220px;width:400px}
.f-email{left:200px;top:288px;width:400px}
.f-phone{left:200px;top:356px;width:400px}
.f-message{left:620px;top:220px;width:400px;height:192px}
.contact .btn{position:absolute;left:530px;top:446px;width:180px;text-align:center}

/* footer */
.site-footer{top:3820px;height:404px;background:var(--grey-bg)}
.footer-brand{position:absolute;left:180px;top:90px;display:flex;align-items:center;gap:10px}
.footer-brand .brand-dot{width:54px;height:54px}
.footer-brand .brand-name{width:130px;font-size:14px}
.footer-col{position:absolute;top:90px}
.footer-col h5{font-size:15px;font-weight:700;text-transform:uppercase;margin-bottom:14px;color:#333}
.footer-col li{list-style:none;font-size:13px;color:#555;line-height:1.9;display:flex;align-items:center;gap:10px}
.footer-col .ico{width:18px;height:18px;border-radius:50%;background:var(--blue)}
.col-news{left:400px}
.col-company{left:660px}
.col-social{left:880px}
.input{width:200px;height:32px;border:1px solid #ccc;background:#fff;font-size:12px;color:#888;padding:7px 10px;margin-bottom:10px}
.copyright{position:absolute;bottom:20px;width:100%;text-align:center;font-size:12px;color:#999}
</style>
</head>
<body>

<header class="site-header">
  <div class="brand"><span class="brand-dot"></span><span class="brand-name">Kindred Pathways Carers Network</span></div>
  <nav class="top-links"><span>MEMBERS</span><span>SUPPORT</span><span>CONTACT</span><span class="social"></span><span class="social"></span></nav>
  <nav class="main-nav"><span>About us</span><span>About Eating Disorders</span><span>Family &amp; Carer Wellbeing</span><span>Services</span><span>Skilled Families</span></nav>
</header>

<section class="hero">
  <div class="hero-photo" role="img" aria-label="Photo of many hands stacked together in a circle"></div>
  <div class="hero-shade"></div>
  <h1 class="hero-title">Welcome to Kindred Pathways<br>Carers Network</h1>
  <div class="hero-actions"><span class="btn btn-green">Member Registration</span><span class="btn btn-magenta">Donate Now</span></div>
  <svg class="save-star" width="54" height="54" viewBox="0 0 24 24"><polygon points="12,2 15,9 22,9.5 16.5,14 18.5,21 12,17 5.5,21 7.5,14 2,9.5 9,9" fill="#6b5a55" stroke="#fff" stroke-width="1.5"/></svg>
  <div class="save-date">SAVE THE DATE<strong>Saturday May 23rd, 2020</strong>FOR RELAY GALA EVENING</div>
  <span class="arrow left"></span><span class="arrow right"></span>
  <svg class="hero-curve" width="1200" height="140" viewBox="0 0 1200 140" preserveAspectRatio="none">
    <path d="M0 60 Q600 170 1200 40 L1200 140 L0 140Z" fill="var(--green)"/>
    <path d="M0 80 Q600 190 1200 60 L1200 140 L0 140Z" fill="#fff"/>
  </svg>
</section>

<section class="about">
  <div class="about-art" role="img" aria-label="Illustration of a family group in purple, blue and red"></div>
  <div class="about-text">
    <h2>ABOUT KPCN</h2>
    <p>Kindred Pathways Carers Network (KPCN) has been established by a group of Australian parents and supporters who have cared for and treated a young person with an eating disorder, to advocate for the needs and roles of other parents during this experience. Parents and families of children under 18 years are seen by the service system to be vital to treatment and recovery.</p>
    <span class="btn btn-magenta">Read More</span>
  </div>
</section>

<section class="informed">
  <svg width="1200" height="540" viewBox="0 0 1200 540" preserveAspectRatio="none" style="position:absolute;inset:0">
    <defs><linearGradient id="plumGrad" x1="0" y1="0" x2="1" y2="1"><stop offset="0" stop-color="#8e2a86"/><stop offset="1" stop-color="#6a1660"/></linearGradient></defs>
    <path d="M0 60 Q600 -20 1200 20 L1200 470 Q600 560 0 500Z" fill="url(#plumGrad)"/>
    <path d="M0 520 Q600 560 1200 440 L1200 470 Q600 570 0 535Z" fill="var(--green)"/>
  </svg>
  <h2>Be Informed</h2>
  <div class="pillars">
    <div class="pillar"><div class="circle"></div><h3>Family and Carer Wellbeing</h3><p>Lorem ipsum dolor sit amet<br>consectetuer adipiscing</p><div class="more"><svg width="16" height="10" viewBox="0 0 16 10"><path d="M1 1 L8 8 L15 1" fill="none" stroke="#fff" stroke-width="2"/></svg></div></div>
    <div class="pillar"><div class="circle"></div><h3>Skilled Families</h3><p>Lorem ipsum dolor sit amet<br>consectetuer adipiscing</p><div class="more"><svg width="16" height="10" viewBox="0 0 16 10"><path d="M1 1 L8 8 L15 1" fill="none" stroke="#fff" stroke-width="2"/></svg></div></div>
    <div class="pillar"><div class="circle"></div><h3>Services &amp; Clinicians</h3><p>Lorem ipsum dolor sit amet<br>consectetuer adipiscing</p><div class="more"><svg width="16" height="10" viewBox="0 0 16 10"><path d="M1 1 L8 8 L15 1" fill="none" stroke="#fff" stroke-width="2"/></svg></div></div>
  </div>
</section>

<section class="cards">
  <div class="card card-groups"><h3>Anchor Carer<br>Support Groups</h3><p>Lorem ipsum dolor sit amet consectetuer adipiscing elit nunc</p><span class="btn btn-green btn-small">Read More</span></div>
  <div class="card card-events"><h3>Upcoming Events</h3><p>Lorem ipsum dolor sit amet consectetuer adipiscing elit nunc</p><span class="btn btn-green btn-small">Read More</span></div>
</section>

<section class="news">
  <h2>Latest News</h2>
  <div class="news-grid">
    <article class="news-item"><div class="news-photo" role="img" aria-label="Photo of hands holding for comfort"></div><h4>Duis non nunc Nulla rhoncus</h4><div class="news-date"><svg width="14" height="14" viewBox="0 0 14 14"><rect x="1" y="2" width="12" height="11" fill="none" stroke="currentColor" stroke-width="1.5"/><line x1="1" y1="5" x2="13" y2="5" stroke="currentColor" stroke-width="1.5"/></svg>JAN 20, 2019</div><p>Duis non nunc nulla rhoncus dictum metus curabitur tristique mi condimentum orci phasellus pellentesque tristique.</p><span class="btn btn-green btn-small">Read More</span></article>
    <article class="news-item"><div class="news-photo" role="img" aria-label="Photo of two people holding hands"></div><h4>Duis non nunc Nulla rhoncus</h4><div class="news-date"><svg width="14" height="14" viewBox="0 0 14 14"><rect x="1" y="2" width="12" height="11" fill="none" stroke="currentColor" stroke-width="1.5"/><line x1="1" y1="5" x2="13" y2="5" stroke="currentColor" stroke-width="1.5"/></svg>JAN 20, 2019</div><p>Duis non nunc nulla rhoncus dictum metus curabitur tristique mi condimentum orci phasellus pellentesque tristique.</p><span class="btn btn-green btn-small">Read More</span></article>
    <article class="news-item"><div class="news-photo" role="img" aria-label="Photo of a group joining hands"></div><h4>Duis non nunc Nulla rhoncus</h4><div class="news-date"><svg width="14" height="14" viewBox="0 0 14 14"><rect x="1" y="2" width="12" height="11" fill="none" stroke="currentColor" stroke-width="1.5"/><line x1="1" y1="5" x2="13" y2="5" stroke="currentColor" stroke-width="1.5"/></svg>JAN 20, 2019</div><p>Duis non nunc nulla rhoncus dictum metus curabitur tristique mi condimentum orci phasellus pellentesque tristique.</p><span class="btn btn-green btn-small">Read More</span></article>
  </div>
</section>

<section class="volunteer">
  <div class="volunteer-text">
    <h2>Can you help us with your time or skills please??</h2>
    <p>Kindred Pathways Carers Network is a volunteer, not for profit organisation, supporting &amp; advocating for parents &amp; carers as they battle to save their loved one from an eating disorder, which are potentially life-threatening mental illnesses.</p>
    <span class="btn btn-magenta">Read More</span>
  </div>
  <div class="volunteer-photo" role="img" aria-label="Photo of volunteers working together at a community event"></div>
</section>

<section class="contact">
  <div class="contact-bg" role="img" aria-label="Green tinted photo of hands joined together"></div>
  <svg width="1200" height="120" viewBox="0 0 1200 120" preserveAspectRatio="none" style="position:absolute;top:0;left:0">
    <path d="M0 0 L1200 0 L1200 30 Q600 130 0 60Z" fill="#fff"/>
  </svg>
  <h2>Contact Form</h2>
  <div class="field f-name">Name</div>
  <div class="field f-email">Email</div>
  <div class="field f-phone">Phone</div>
  <div class="field f-message">Message</div>
  <span class="btn btn-magenta">Submit Now</span>
</section>

<footer class="site-footer">
  <svg width="1200" height="80" viewBox="0 0 1200 80" preserveAspectRatio="none" style="position:absolute;top:0;left:0">
    <path d="M0 0 L1200 0 L1200 10 Q600 90 0 30Z" fill="#4ea51c"/>
  </svg>
  <div class="footer-brand"><span class="brand-dot"></span><span class="brand-name">Kindred Pathways Carers Network</span></div>
  <div class="footer-col col-news"><h5>Join Newsletters</h5><div class="input">Name</div><div class="input">Email address</div><span class="btn btn-green btn-small">Submit Now</span></div>
  <div class="footer-col col-company"><h5>Company</h5><ul><li>About us</li><li>Services</li><li>Family and Carer Wellbeing</li><li>Skilled Families</li><li>Contact</li></ul></div>
  <div class="footer-col col-social"><h5>Get Connected</h5><ul><li><span class="ico"></span>Chirpline</li><li><span class="ico"></span>Friendboard</li><li><span class="ico"></span>Careerlink</li><li><span class="ico"></span>Snapgram</li></ul></div>
  <p class="copyright">Copyright © 2019 All rights reserved</p>
</footer>

</body>
</html>
```